Providing Back Office Solutions to Financial Advisors and Attorney Needs a Business Card Design

Need a Business Card Design that speaks to Financial Advisor and Attorneys. Some of the word that come to mind is Clean/Simple & Futuristic.

Industry/Entity Type

Business

```html
<!DOCTYPE html>
<html lang="en">
<head>
<meta charset="UTF-8">
<title>Corvane Business Card</title>
<link href="https://fonts.googleapis.com/css2?family=Roboto+Condensed:wght@300;400;500&display=swap" rel="stylesheet">
<style>
  :root {
    --page-bg: #eef0f0;
    --card-blue: #008dd6;
    --ink-white: #ffffff;
    --tagline-blue: #86c9ee;
    --divider-blue: #3aa6df;
  }
  * { margin: 0; padding: 0; box-sizing: border-box; }
  html, body {
    width: 1200px;
    height: 1200px;
    overflow: hidden;
    background: var(--page-bg);
    font-family: "Roboto Condensed", "Arial Narrow", sans-serif;
  }
  .business-card {
    position: absolute;
    left: 286px;
    top: 421px;
    width: 628px;
    height: 359px;
    background: var(--card-blue);
    color: var(--ink-white);
  }
  .brand {
    position: absolute;
    left: 55px;
    top: 190px;
    width: 200px;
    text-align: center;
  }
  .brand-name {
    display: flex;
    align-items: center;
    justify-content: center;
    gap: 10px;
    font-weight: 500;
    font-size: 42px;
    letter-spacing: 2px;
    line-height: 1;
    color: var(--ink-white);
  }
  .brand-mark {
    width: 26px;
    height: 26px;
    background: var(--ink-white);
    flex: none;
  }
  .brand-tagline {
    margin-top: 6px;
    font-weight: 400;
    font-size: 17.5px;
    letter-spacing: 0.4px;
    color: var(--tagline-blue);
    white-space: nowrap;
  }
  .divider {
    position: absolute;
    left: 318px;
    top: 92px;
    width: 2px;
    height: 170px;
    background: var(--divider-blue);
  }
  .contact {
    position: absolute;
    left: 410px;
    top: 90px;
    font-weight: 300;
    font-size: 21px;
    line-height: 26px;
    white-space: nowrap;
  }
  .contact-name { margin-bottom: 11px; }
  .contact-address { margin-bottom: 16px; }
  .contact-email { line-height: 22px; }
</style>
</head>
<body>
  <section class="business-card">
    <div class="brand">
      <div class="brand-name"><span class="brand-mark"></span>CORVANE</div>
      <div class="brand-tagline">BACK OFFICE SOLUTIONS</div>
    </div>
    <div class="divider"></div>
    <div class="contact">
      <p class="contact-name">Dana Whitlock - MD</p>
      <p class="contact-address">2718 Harbor Street<br>Millbrook, FL 32100</p>
      <p class="contact-phone">555-014-2288<br>555-019-7731</p>
      <p class="contact-email">whitlock@corvane.com</p>
    </div>
  </section>
</body>
</html>
```